Vantage Sport And Fitness- Rates

I am opening up a new Gym/Training Facility. The Name of my New gym is Vantage Sports And Fitness. I am wanting to design a card that captures Membership Pricing/Personal Training Pricing. I will Upload the Logo. My colors are Red/Black/Silver. I really want there pricing card to "POP". IT needs to be very Professional and Clean. I will be placing these cards on a 5'7 . I would like these item on the card:
Name of Company: Vantage Sports And Fitness
Address:
2817 Larkmoor Commerce Dr.
Suite 214 Fernvale, OH 43210
Phone #: 614-555-0187
website: www.vantagesnf-example.com
Membership Rates:
$99/Month
$49 Heroes Rate
Family Plan:
2 People $149
3 People $199
4 People $299
Personal Training Rates:
1 session $102
5 sessions $490
10 sessions $940
20 sessions $1,800
40 sessions $3,400
Please be creative

```html
<!DOCTYPE html>
<html lang="en">
<head>
<meta charset="utf-8">
<title>Vantage Sports And Fitness – Rates</title>
<link rel="stylesheet" href="https://fonts.googleapis.com/css2?family=Open+Sans:wght@600;700&family=Roboto:wght@400;500;700&display=swap">
<style>
  :root {
    --backdrop: #5a5a5c;
    --paper: #ffffff;
    --brand-red: #d2232a;
    --charcoal: #3d3d3f;
    --ink: #404042;
    --photo-dark: #1c1d20;
  }
  html, body {
    margin: 0;
    padding: 0;
    width: 916px;
    height: 1200px;
    overflow: hidden;
    background: var(--backdrop);
  }
  .rate-card {
    display: block;
    width: 916px;
    height: 1200px;
  }
  .title-main {
    font-family: "Open Sans", sans-serif;
    font-weight: 700;
    fill: var(--brand-red);
  }
  .title-sub {
    font-family: "Open Sans", sans-serif;
    font-weight: 700;
    fill: var(--ink);
  }
  .band-heading {
    font-family: "Roboto", sans-serif;
    font-weight: 500;
    font-size: 24px;
    fill: var(--paper);
  }
  .price-line {
    font-family: "Roboto", sans-serif;
    font-weight: 500;
    font-size: 21px;
    fill: var(--paper);
  }
  .brand-name {
    font-family: "Roboto", sans-serif;
    font-weight: 400;
    fill: var(--brand-red);
  }
  .contact-line {
    font-family: "Roboto", sans-serif;
    font-weight: 400;
    font-size: 18px;
    fill: var(--ink);
  }
  .phone-number {
    font-family: "Roboto", sans-serif;
    font-weight: 400;
    font-size: 39px;
    fill: var(--paper);
  }
</style>
</head>
<body>
<svg class="rate-card" viewBox="0 0 1145 1500" xmlns="http://www.w3.org/2000/svg">
  <!-- sheet -->
  <rect class="sheet-shadow" x="107" y="96" width="935" height="1323" fill="#3a3a3c" opacity="0.6"/>
  <rect class="sheet" x="103" y="91" width="935" height="1323" fill="var(--paper)"/>

  <!-- header -->
  <polygon class="header-edge" points="103,91 148,91 103,280" fill="var(--charcoal)"/>
  <polygon class="header-stripe" points="148,91 162,91 112,295 103,295 103,280" fill="var(--brand-red)"/>
  <polygon class="header-corner" points="853,91 1038,91 1038,295 805,295" fill="var(--brand-red)"/>
  <text class="title-main" x="455" y="195" font-size="70" letter-spacing="7" text-anchor="middle">VANTAGE</text>
  <text class="title-sub" x="464" y="252" font-size="43" letter-spacing="5" text-anchor="middle">SPORTS AND FITNESS</text>

  <!-- photo panels -->
  <defs>
    <linearGradient id="photoLeft" x1="0" y1="0" x2="1" y2="1">
      <stop offset="0" stop-color="#25282c"/>
      <stop offset="0.55" stop-color="#6b4f42"/>
      <stop offset="1" stop-color="var(--photo-dark)"/>
    </linearGradient>
    <linearGradient id="photoRight" x1="0" y1="0" x2="1" y2="1">
      <stop offset="0" stop-color="#c7b59c"/>
      <stop offset="0.5" stop-color="#d8c2b0"/>
      <stop offset="1" stop-color="#5b5d63"/>
    </linearGradient>
  </defs>
  <polygon class="photo-strength" role="img" aria-label="Athlete training with dumbbells in a dark studio" points="103,296 617,296 530,676 103,676" fill="url(#photoLeft)"/>
  <polygon class="photo-yoga" role="img" aria-label="Group of people meditating in a yoga class" points="626,296 1038,296 1038,676 540,676" fill="url(#photoRight)"/>
  <polygon class="photo-tint" points="103,613 745,613 731,676 103,676" fill="var(--brand-red)" opacity="0.35"/>

  <!-- membership rates -->
  <polygon class="band-dark" points="103,676 748,676 735,736 103,736" fill="var(--charcoal)"/>
  <polygon class="band-edge" points="705,736 735,736 710,760 690,832 680,832" fill="var(--charcoal)"/>
  <polygon class="band-red" points="103,736 705,736 680,832 103,832" fill="var(--brand-red)"/>
  <text class="band-heading" x="355" y="715" text-anchor="middle">Membership Rates</text>
  <text class="price-line" x="358" y="776" text-anchor="middle">$99/Month</text>
  <text class="price-line" x="358" y="812" text-anchor="middle">$49 Heroes Rate</text>

  <!-- family plan -->
  <polygon class="band-dark" points="103,834 706,834 692,892 103,892" fill="var(--charcoal)"/>
  <polygon class="band-edge" points="662,892 692,892 668,915 632,1042 622,1042" fill="var(--charcoal)"/>
  <polygon class="band-red" points="103,892 662,892 622,1042 103,1042" fill="var(--brand-red)"/>
  <text class="band-heading" x="355" y="871" text-anchor="middle">Family Plan</text>
  <text class="price-line" x="358" y="932" text-anchor="middle">2 People $149</text>
  <text class="price-line" x="358" y="974" text-anchor="middle">3 People $199</text>
  <text class="price-line" x="355" y="1016" text-anchor="middle">4 People $299</text>

  <!-- personal training -->
  <polygon class="band-dark" points="103,1044 650,1044 636,1102 103,1102" fill="var(--charcoal)"/>
  <polygon class="band-edge" points="608,1102 636,1102 612,1124 560,1316 548,1316" fill="var(--charcoal)"/>
  <polygon class="band-red" points="103,1102 608,1102 548,1316 103,1316" fill="var(--brand-red)"/>
  <text class="band-heading" x="357" y="1081" text-anchor="middle">Personal Training Rates</text>
  <text class="price-line" x="358" y="1146" text-anchor="middle">1 session $102</text>
  <text class="price-line" x="358" y="1183" text-anchor="middle">5 sessions $490</text>
  <text class="price-line" x="358" y="1220" text-anchor="middle">10 sessions $940</text>
  <text class="price-line" x="358" y="1259" text-anchor="middle">20 sessions $1,800</text>
  <text class="price-line" x="355" y="1297" text-anchor="middle">40 sessions $3,400</text>

  <!-- brand block -->
  <circle class="brand-dot" cx="742" cy="955" r="36" fill="var(--brand-red)"/>
  <text class="brand-name" x="792" y="965" font-size="42">VANTAGE</text>
  <text class="brand-name" x="793" y="982" font-size="13" letter-spacing="3.2">SPORTS AND FITNESS</text>

  <!-- contact -->
  <g class="icon-pin" fill="var(--brand-red)">
    <path d="M710 1064 a11 11 0 0 1 11 11 c0 8 -11 16 -11 16 s-11 -8 -11 -16 a11 11 0 0 1 11 -11z"/>
    <circle cx="710" cy="1075" r="4.5" fill="var(--paper)"/>
  </g>
  <text class="contact-line" x="751" y="1072">2817 Larkmoor Commerce Dr.</text>
  <text class="contact-line" x="751" y="1095">Suite 214 Fernvale, OH 43210</text>

  <g class="icon-globe" fill="none" stroke="var(--brand-red)" stroke-width="2">
    <circle cx="710" cy="1136" r="9.5"/>
    <ellipse cx="710" cy="1136" rx="4" ry="9.5"/>
    <line x1="700.5" y1="1136" x2="719.5" y2="1136"/>
    <line x1="702" y1="1131" x2="718" y2="1131"/>
    <line x1="702" y1="1141" x2="718" y2="1141"/>
  </g>
  <text class="contact-line" x="751" y="1141">www.vantagesnf-example.com</text>

  <!-- phone bar -->
  <polygon class="phone-shadow" points="668,1276 1038,1276 1038,1290 655,1290 683,1192" fill="var(--charcoal)"/>
  <polygon class="phone-bar" points="683,1192 1038,1192 1038,1276 668,1276" fill="var(--brand-red)"/>
  <path class="icon-phone" fill="var(--paper)" d="M707 1222 l7 -2 l6 11 l-5 4 c2 5 6 9 11 11 l4 -5 l11 6 l-2 7 c-16 1 -33 -16 -32 -32z"/>
  <text class="phone-number" x="751" y="1250">614-555-0187</text>

  <!-- footer bands -->
  <polygon class="footer-dark" points="103,1328 570,1316 1038,1328 1038,1388 103,1392" fill="var(--charcoal)"/>
  <polygon class="footer-red" points="103,1392 1038,1388 1038,1396 515,1404 515,1414 103,1414" fill="var(--brand-red)"/>
</svg>
</body>
</html>
```